Demo Screens Needed for Recruiting with AI App

We are in the process of raising money for our startup called PylonGrove. We need demos to show investors what we're trying to do with images. We really love the simplicity and modern look of the Lantern App and want something similar. We will have the "swipe" functionality similar to Kindle as well. The sample images I've attached are only for caregivers but long term this will be for all industries. There will also be a rewards page for loyalty membership. The current landing page is www.pylongrove.example. That will show you the color scheme and logo.

```html
<!DOCTYPE html>
<html lang="en">
<head>
<meta charset="utf-8">
<title>PylonGrove – App Screens</title>
<link href="https://fonts.googleapis.com/css2?family=Poppins:wght@300;400;500&display=swap" rel="stylesheet">
<style>
  :root{
    --bg-a:#c9b4f2;
    --bg-b:#bfe2f5;
    --night:#07040f;
    --violet:#2a1566;
    --violet-deep:#1b0c45;
    --teal:#1d4a6e;
    --white:#ffffff;
    --soft:#e9e4f7;
    --star:#f08a1c;
    --heart:#e8163b;
    --nav:#050308;
  }
  *{box-sizing:border-box;margin:0;padding:0}
  html,body{width:1200px;height:800px;overflow:hidden}
  body{
    font-family:"Poppins",sans-serif;color:var(--white);
    background:linear-gradient(120deg,var(--bg-a) 0%,#c4c9f4 50%,var(--bg-b) 100%);
    position:relative;
  }
  .screen{
    position:absolute;top:62px;width:300px;height:650px;overflow:hidden;
    background:linear-gradient(180deg,var(--night) 0%,var(--violet-deep) 35%,var(--violet) 62%,var(--teal) 100%);
  }
  .screen--welcome{left:106px}
  .screen--browse{left:450px}
  .screen--profile{left:794px}
  .abs{position:absolute}
  .status{position:absolute;top:14px;left:10px;right:10px;height:12px;font-size:9px;display:flex;justify-content:space-between;align-items:center}
  .status svg{height:9px}
  .brand{font-weight:300;letter-spacing:3px;color:var(--white);text-transform:uppercase;white-space:nowrap}
  .welcome-brand{left:0;right:0;top:140px;text-align:center;font-size:26px;letter-spacing:4px}
  .tagline{left:0;right:0;text-align:center;font-weight:400}
  .tagline--one{top:242px;font-size:13px;letter-spacing:.5px}
  .tagline--two{top:267px;font-size:12.5px;letter-spacing:3.2px}
  .rule{top:300px;left:127px;width:46px;height:2px;background:var(--white)}
  .cta{left:19px;top:480px;width:266px;height:42px;border-radius:21px;background:var(--white);color:#111;
    display:flex;align-items:center;justify-content:center;font-size:12px;font-weight:500;letter-spacing:.3px}
  .signin{left:0;right:0;top:541px;text-align:center;font-size:12px;font-weight:500;letter-spacing:.5px;color:#d6d2ee}
  .top-brand{top:44px;font-size:18px}
  .grid-btn{left:263px;top:42px;width:26px;height:26px;border-radius:50%;background:var(--white);display:flex;align-items:center;justify-content:center}
  .card{position:absolute;width:130px;text-align:center}
  .photo{width:130px;height:135px;border:2px solid var(--white);border-radius:8px}
  .card-name{font-size:12px;margin-top:8px}
  .card-meta{font-size:9.5px;margin-top:3px}
  .card-rate{font-size:11px;margin-top:4px}
  .stars{color:var(--star);font-size:7px;letter-spacing:.5px;line-height:1}
  .card .stars{margin-top:4px}
  .nav{position:absolute;left:0;right:0;bottom:0;height:50px;background:var(--nav)}
  .nav-btn{position:absolute;top:7px;width:36px;height:36px;border-radius:50%;background:var(--white);border:2px solid #777;display:flex;align-items:center;justify-content:center}
  .nav-btn svg{width:16px;height:16px;fill:#111}
  .back{left:18px;top:46px;display:flex;align-items:center;gap:8px;font-size:11px}
  .hero{left:14px;top:79px;width:271px;height:515px;border-radius:4px;
    background:linear-gradient(180deg,#d9d6d2 0%,#b7a398 30%,#8a7c78 50%,#5b6a6a 62%,#3a2a6e 80%,#2a1566 100%)}
  .actions{left:0;right:0;top:352px;display:flex;justify-content:center;gap:16px}
  .action{width:40px;height:40px;border-radius:50%;background:var(--white);border:2px solid #ccc;display:flex;align-items:center;justify-content:center}
  .action svg{width:20px;height:20px}
  .profile-info{left:0;right:0;top:412px;text-align:center;font-size:11px}
  .profile-info .row{display:flex;justify-content:center;align-items:center;gap:5px;height:21.5px}
  .profile-info .row svg{width:10px;height:10px;fill:var(--white)}
  .profile-name{font-size:13px;margin-bottom:2px}
  .handle{left:83px;top:592px;width:135px;height:4px;border-radius:2px;background:var(--white)}
</style>
</head>
<body>

<!-- Welcome screen -->
<section class="screen screen--welcome">
  <div class="status"><span>10.40</span>
    <svg viewBox="0 0 48 10"><g fill="#fff"><rect x="0" y="6" width="1.6" height="4"/><rect x="3" y="4" width="1.6" height="6"/><rect x="6" y="2" width="1.6" height="8"/><rect x="9" y="0" width="1.6" height="10"/><path d="M15 4a8 8 0 0 1 11 0l-1.3 1.3a6 6 0 0 0-8.4 0zM18 7a4 4 0 0 1 5 0l-2.5 2.6z"/><rect x="30" y="1" width="16" height="8" rx="2.5" fill="none" stroke="#fff" stroke-width="1.2"/><rect x="32" y="3" width="12" height="4" rx="1"/></g></svg>
  </div>
  <div class="abs brand welcome-brand">PylonGrove</div>
  <p class="abs tagline tagline--one">UNLOCKING THE POWER OF</p>
  <p class="abs tagline tagline--two">MEANINGFUL CONNECTIONS</p>
  <div class="abs rule"></div>
  <div class="abs cta">CREATE AN ACCOUNT</div>
  <div class="abs signin">SIGN IN</div>
</section>

<!-- Browse screen -->
<section class="screen screen--browse">
  <div class="status"><span>10.40</span>
    <svg viewBox="0 0 48 10"><g fill="#fff"><rect x="0" y="6" width="1.6" height="4"/><rect x="3" y="4" width="1.6" height="6"/><rect x="6" y="2" width="1.6" height="8"/><rect x="9" y="0" width="1.6" height="10"/><path d="M15 4a8 8 0 0 1 11 0l-1.3 1.3a6 6 0 0 0-8.4 0zM18 7a4 4 0 0 1 5 0l-2.5 2.6z"/><rect x="30" y="1" width="16" height="8" rx="2.5" fill="none" stroke="#fff" stroke-width="1.2"/><rect x="32" y="3" width="12" height="4" rx="1"/></g></svg>
  </div>
  <div class="abs brand top-brand" style="left:13px">PylonGrove</div>
  <div class="abs grid-btn"><svg width="12" height="12" viewBox="0 0 12 12" fill="#111"><rect x="0" y="0" width="3" height="3"/><rect x="4.5" y="0" width="3" height="3"/><rect x="9" y="0" width="3" height="3"/><rect x="0" y="4.5" width="3" height="3"/><rect x="4.5" y="4.5" width="3" height="3"/><rect x="9" y="4.5" width="3" height="3"/><rect x="0" y="9" width="3" height="3"/><rect x="4.5" y="9" width="3" height="3"/><rect x="9" y="9" width="3" height="3"/></svg></div>

  <article class="card" style="left:15px;top:82px">
    <div class="photo" role="img" aria-label="Portrait photo of caregiver Maren T outdoors at sunset" style="background:linear-gradient(160deg,#6b7a3a,#c98a3c 55%,#7a3a24)"></div>
    <p class="card-name">Maren T</p><p class="card-meta">From: Palo Alto, CA</p><p class="card-rate">$25 per/hr</p><p class="stars">★★★★★</p>
  </article>
  <article class="card" style="left:155px;top:82px">
    <div class="photo" role="img" aria-label="Photo of caregiver Delia R seated on a sofa" style="background:linear-gradient(170deg,#e6e6e6,#c9c07a 55%,#6f8aa8)"></div>
    <p class="card-name">Delia R</p><p class="card-meta">From: Los Altos, CA</p><p class="card-rate">$25 per/hr</p><p class="stars">★★★★★</p>
  </article>
  <article class="card" style="left:15px;top:302px">
    <div class="photo" role="img" aria-label="Portrait photo of caregiver Noor K in a warm sweater" style="background:linear-gradient(160deg,#b08a6e,#a0603a 60%,#7a4128)"></div>
    <p class="card-name">Noor K</p><p class="card-meta">From: Palo Alto, CA</p><p class="card-rate">$25 per/hr</p><p class="stars">★★★★★</p>
  </article>
  <article class="card" style="left:155px;top:302px">
    <div class="photo" role="img" aria-label="Photo of caregiver Lina P working at a laptop" style="background:linear-gradient(170deg,#f0ece8,#d9b8a8 55%,#9fc6cc)"></div>
    <p class="card-name">Lina P</p><p class="card-meta">From: Palo Alto, CA</p><p class="card-rate">$25 per/hr</p><p class="stars">★★★★★</p>
  </article>
  <article class="card" style="left:15px;top:522px">
    <div class="photo" role="img" aria-label="Photo of a caregiver in a home office" style="background:linear-gradient(170deg,#d8c7aa,#b49274 60%,#8c6a50)"></div>
  </article>
  <article class="card" style="left:155px;top:522px">
    <div class="photo" role="img" aria-label="Photo of a caregiver in an office" style="background:linear-gradient(170deg,#dfe3ea,#8f98a8 55%,#2b2a30)"></div>
  </article>

  <nav class="nav">
    <span class="nav-btn" style="left:28px"><svg viewBox="0 0 16 16"><path d="M8 1.5 0.5 8h2v6.5h4v-4h3v4h4V8h2z"/></svg></span>
    <span class="nav-btn" style="left:98px"><svg viewBox="0 0 16 16"><path d="M6.5 1a5.5 5.5 0 0 1 4.4 8.8l4 4-1.4 1.4-4-4A5.5 5.5 0 1 1 6.5 1zm0 2a3.5 3.5 0 1 0 0 7 3.5 3.5 0 0 0 0-7z"/></svg></span>
    <span class="nav-btn" style="left:166px"><svg viewBox="0 0 16 16"><rect x="1" y="1" width="6" height="6" rx="1"/><rect x="9" y="1" width="6" height="6" rx="1"/><rect x="1" y="9" width="6" height="6" rx="1"/><rect x="9" y="9" width="6" height="6" rx="1"/></svg></span>
    <span class="nav-btn" style="left:236px"><svg viewBox="0 0 16 16"><circle cx="8" cy="4.5" r="3.5"/><path d="M1.5 15.5c0-4 3-6 6.5-6s6.5 2 6.5 6z"/></svg></span>
  </nav>
</section>

<!-- Profile screen -->
<section class="screen screen--profile">
  <div class="status"><span>10.40</span>
    <svg viewBox="0 0 48 10"><g fill="#fff"><rect x="0" y="6" width="1.6" height="4"/><rect x="3" y="4" width="1.6" height="6"/><rect x="6" y="2" width="1.6" height="8"/><rect x="9" y="0" width="1.6" height="10"/><path d="M15 4a8 8 0 0 1 11 0l-1.3 1.3a6 6 0 0 0-8.4 0zM18 7a4 4 0 0 1 5 0l-2.5 2.6z"/><rect x="30" y="1" width="16" height="8" rx="2.5" fill="none" stroke="#fff" stroke-width="1.2"/><rect x="32" y="3" width="12" height="4" rx="1"/></g></svg>
  </div>
  <div class="abs back"><svg width="20" height="10" viewBox="0 0 20 10" fill="none" stroke="#fff" stroke-width="1.2"><path d="M19 5H1M5 1 1 5l4 4"/></svg>Back</div>
  <div class="abs brand top-brand" style="right:16px">PylonGrove</div>

  <div class="abs hero" role="img" aria-label="Large portrait photo of caregiver Lina P smiling indoors"></div>

  <div class="abs actions">
    <span class="action"><svg viewBox="0 0 20 20"><path fill="var(--heart)" d="M10 18 2.5 10.5A4.6 4.6 0 0 1 10 4.6a4.6 4.6 0 0 1 7.5 5.9z"/></svg></span>
    <span class="action"><svg viewBox="0 0 20 20"><path fill="var(--star)" d="m10 1.5 2.6 5.5 6 .7-4.4 4.1 1.2 6-5.4-3-5.4 3 1.2-6L1.4 7.7l6-.7z"/></svg></span>
    <span class="action"><svg viewBox="0 0 20 20"><path stroke="var(--heart)" stroke-width="3.4" stroke-linecap="round" d="M5 5l10 10M15 5 5 15"/></svg></span>
  </div>

  <div class="abs profile-info">
    <p class="profile-name">Lina P</p>
    <p class="row"><svg viewBox="0 0 16 16"><path d="M8 1.5 0.5 8h2v6.5h4v-4h3v4h4V8h2z"/></svg>Palo Alto, CA</p>
    <p class="row"><svg viewBox="0 0 16 16"><path d="M1 2h9v9H1zM6 5h9v9H6z" fill-opacity=".85"/></svg>English, Spanish</p>
    <p class="row"><svg viewBox="0 0 16 16"><path d="M4 1h10l-2 14H2z"/></svg>Bachelor’s Degree</p>
    <p class="row">$25 per/hr</p>
    <p class="row stars">★★★★★</p>
    <p class="row"><svg viewBox="0 0 10 10" style="width:8px;height:8px"><path d="M1 1l4 3 4-3M1 5l4 3 4-3" fill="none" stroke="#fff" stroke-width="1.4"/></svg></p>
  </div>
  <div class="abs handle"></div>

  <nav class="nav">
    <span class="nav-btn" style="left:28px"><svg viewBox="0 0 16 16"><path d="M8 1.5 0.5 8h2v6.5h4v-4h3v4h4V8h2z"/></svg></span>
    <span class="nav-btn" style="left:98px"><svg viewBox="0 0 16 16"><path d="M6.5 1a5.5 5.5 0 0 1 4.4 8.8l4 4-1.4 1.4-4-4A5.5 5.5 0 1 1 6.5 1zm0 2a3.5 3.5 0 1 0 0 7 3.5 3.5 0 0 0 0-7z"/></svg></span>
    <span class="nav-btn" style="left:166px"><svg viewBox="0 0 16 16"><rect x="1" y="1" width="6" height="6" rx="1"/><rect x="9" y="1" width="6" height="6" rx="1"/><rect x="1" y="9" width="6" height="6" rx="1"/><rect x="9" y="9" width="6" height="6" rx="1"/></svg></span>
    <span class="nav-btn" style="left:236px"><svg viewBox="0 0 16 16"><circle cx="8" cy="4.5" r="3.5"/><path d="M1.5 15.5c0-4 3-6 6.5-6s6.5 2 6.5 6z"/></svg></span>
  </nav>
</section>

</body>
</html>
```